Creative Businesss Card desgin!

Create a business card for our business Gleam window cleaning!
We are open to creative ideas as long as it maintains a professional image.

Target Market(s)

Small Commercial window cleaning clients including car dealerships, strata manager, cafe

Industry/Entity Type

Window Cleaning

Contact Information for Business Card

Daniel Prescott
General Manager
Gleam Window Cleaning

daniel@gleamservices.com.au
pane-care-southbank.com.au
Ph: 1800 GET GLEAM
Mob: 0437 582 061

Colors
fbed22
0392cd

Requirements
Should not have
• Stock window cleaning/ squeegee graphics

```html
<!DOCTYPE html>
<html lang="en">
<head>
<meta charset="utf-8">
<title>Gleam Window Cleaning – Business Card</title>
<link rel="stylesheet" href="https://fonts.googleapis.com/css2?family=Open+Sans:wght@400;600;700&display=swap">
<style>
  :root {
    --page-bg: #e9e6e1;
    --card-blue: #0a5d8f;
    --card-blue-light: #1a72a6;
    --card-blue-dark: #074a74;
    --brand-yellow: #fbed22;
    --card-shadow: rgba(20, 30, 40, 0.28);
  }
  * { margin: 0; padding: 0; box-sizing: border-box; }
  html, body {
    width: 1200px;
    height: 800px;
    overflow: hidden;
  }
  body {
    background: var(--page-bg);
    font-family: "Open Sans", Arial, sans-serif;
    display: flex;
    align-items: center;
    justify-content: center;
    gap: 40px;
  }
  .card {
    position: relative;
    width: 540px;
    height: 309px;
    background: radial-gradient(circle at 30% 20%, var(--card-blue-light), var(--card-blue) 55%, var(--card-blue-dark));
    box-shadow: 0 14px 30px var(--card-shadow);
    color: var(--brand-yellow);
    overflow: hidden;
  }

  /* Front */
  .card-front {
    display: flex;
    align-items: center;
    justify-content: center;
  }
  .wordmark {
    font-weight: 700;
    text-transform: uppercase;
    color: var(--brand-yellow);
    line-height: 1;
  }
  .card-front .wordmark-name {
    display: block;
    font-size: 92px;
    letter-spacing: 4px;
  }
  .card-front .wordmark-tag {
    display: block;
    font-size: 24px;
    letter-spacing: 1px;
    margin-top: 8px;
    text-align: right;
  }

  /* Back */
  .card-back .back-wordmark {
    position: absolute;
    left: 34px;
    bottom: 44px;
  }
  .card-back .wordmark-name {
    display: block;
    font-size: 50px;
    letter-spacing: 2px;
  }
  .card-back .wordmark-tag {
    display: block;
    font-size: 13px;
    margin-top: 5px;
    text-align: right;
  }
  .divider {
    position: absolute;
    left: 262px;
    top: 60px;
    width: 1.5px;
    height: 190px;
    background: var(--brand-yellow);
  }
  .contact-block {
    position: absolute;
    left: 286px;
    top: 62px;
  }
  .person-name {
    font-size: 19px;
    font-weight: 600;
    text-transform: uppercase;
    letter-spacing: 0.3px;
  }
  .person-role {
    font-size: 11px;
    margin-top: 1px;
  }
  .contact-list {
    list-style: none;
    margin-top: 20px;
    font-size: 12px;
  }
  .contact-list li {
    display: flex;
    align-items: center;
    gap: 8px;
    height: 18px;
  }
  .contact-list li.gap-before { margin-top: 14px; }
  .contact-icon {
    width: 11px;
    height: 11px;
    flex: none;
  }
</style>
</head>
<body>

  <section class="card card-front" aria-label="Business card front">
    <div class="wordmark">
      <span class="wordmark-name">Gleam</span>
      <span class="wordmark-tag">Window Cleaning</span>
    </div>
  </section>

  <section class="card card-back" aria-label="Business card back">
    <div class="wordmark back-wordmark">
      <span class="wordmark-name">Gleam</span>
      <span class="wordmark-tag">Window Cleaning</span>
    </div>

    <div class="divider"></div>

    <div class="contact-block">
      <p class="person-name">Daniel Prescott</p>
      <p class="person-role">General manager</p>

      <ul class="contact-list">
        <li>
          <svg class="contact-icon" viewBox="0 0 12 12" aria-hidden="true"><path d="M2.5 1 L4.5 1 L5.2 3.4 L4 4.4 C4.6 5.8 6.2 7.4 7.6 8 L8.6 6.8 L11 7.5 L11 9.5 C11 10.3 10.3 11 9.5 11 C5 11 1 7 1 2.5 C1 1.7 1.7 1 2.5 1 Z" fill="currentColor"/></svg>
          <span>1800 GET GLEAM</span>
        </li>
        <li>
          <svg class="contact-icon" viewBox="0 0 12 12" aria-hidden="true"><rect x="3" y="0.5" width="6" height="11" rx="1" fill="none" stroke="currentColor" stroke-width="1.2"/><circle cx="6" cy="9.5" r="0.7" fill="currentColor"/></svg>
          <span>0437 582 061</span>
        </li>
        <li class="gap-before">
          <svg class="contact-icon" viewBox="0 0 12 12" aria-hidden="true"><rect x="0.6" y="2.2" width="10.8" height="7.6" fill="none" stroke="currentColor" stroke-width="1.1"/><path d="M0.8 2.6 L6 6.6 L11.2 2.6" fill="none" stroke="currentColor" stroke-width="1.1"/></svg>
          <span>daniel@gleamservices.com.au</span>
        </li>
        <li>
          <svg class="contact-icon" viewBox="0 0 12 12" aria-hidden="true"><circle cx="6" cy="6" r="5.2" fill="none" stroke="currentColor" stroke-width="1.1"/><ellipse cx="6" cy="6" rx="2.3" ry="5.2" fill="none" stroke="currentColor" stroke-width="1"/><path d="M0.8 6 H11.2 M1.8 3.4 H10.2 M1.8 8.6 H10.2" stroke="currentColor" stroke-width="0.9"/></svg>
          <span>pane-care-southbank.com.au</span>
        </li>
      </ul>
    </div>
  </section>

</body>
</html>
```